Medical Billing Company Needs a Business Card Design

We need a business card design for a Florida based medical billing company called 'Medora Crestline Solutions'. We specialize in providing revenue cycle management services to physician and therapist offices (we're basically their back-office processing partner for providing billing software, claims submissions, A/R follow-up and patient statements & collections. Our logo is red and blue-ish, so make sure that whatever other elements are used will match appropriately. Our current business card design has a too small font size. I'd like to project an image that shows we are modern & reliable. On a side note, I'm planning on using ZIB for printing these cards.

Target Market(s)

Office managers, physicians, therapists

Industry/Entity Type

Printing

Requirements
Must have
• Logo
Name of Employee
Phone
Fax
E-mail
Website

```html
<!DOCTYPE html>
<html lang="en">
<head>
<meta charset="utf-8">
<title>Medora Crestline Solutions – Business Card</title>
<link rel="stylesheet" href="https://fonts.googleapis.com/css2?family=Open+Sans:wght@400;600;700&display=swap">
<style>
  :root {
    --stage-bg: #ecebef;
    --card-white: #ffffff;
    --navy: #2a1d78;
    --brand-red: #a3232f;
    --ink: #4a4a55;
    --violet-light: #5f4ea3;
    --violet-deep: #1e0b6b;
    --on-dark: #ffffff;
  }
  * { box-sizing: border-box; margin: 0; padding: 0; }
  html, body {
    width: 1200px; height: 720px; overflow: hidden;
    background: var(--stage-bg);
    font-family: "Open Sans", Arial, sans-serif;
  }
  .stage {
    width: 1200px; height: 720px;
    display: flex; align-items: center; justify-content: center; gap: 40px;
  }
  .card {
    width: 540px; height: 309px; position: relative;
    border-radius: 4px; overflow: hidden;
    box-shadow: 0 6px 18px rgba(0,0,0,.18);
  }

  /* Front */
  .card-front { background: var(--card-white); }
  .brand-name {
    position: absolute; left: 36px; top: 58px;
    font-size: 25px; font-weight: 600; letter-spacing: 2.5px;
    color: var(--navy); white-space: nowrap;
  }
  .holder {
    position: absolute; right: 40px; top: 122px; text-align: left;
  }
  .holder-name { font-size: 19px; font-weight: 700; color: var(--navy); line-height: 1.1; }
  .holder-title { font-size: 13px; color: var(--brand-red); margin-left: 46px; }
  .contact-list {
    position: absolute; left: 36px; top: 176px; list-style: none;
    font-size: 13px; color: var(--ink); line-height: 19px;
  }
  .contact-list li { display: flex; align-items: center; gap: 7px; }
  .contact-list svg { width: 11px; height: 11px; fill: var(--navy); flex: none; }
  .address {
    position: absolute; left: 36px; top: 258px;
    font-size: 13px; color: var(--ink); line-height: 18px; font-style: normal;
  }

  /* Back */
  .card-back {
    background: linear-gradient(115deg, var(--violet-light) 0%, var(--violet-deep) 100%);
    color: var(--on-dark);
  }
  .back-mark {
    position: absolute; left: 0; right: 0; top: 108px;
    display: flex; align-items: center; justify-content: center; gap: 14px;
  }
  .back-mark .square {
    width: 22px; height: 22px; border: 2px solid var(--on-dark);
  }
  .back-mark .brand-name-light {
    font-size: 26px; font-weight: 600; letter-spacing: 3px; white-space: nowrap;
  }
  .back-url {
    position: absolute; left: 0; right: 0; top: 212px; text-align: center;
    font-size: 16px; letter-spacing: 3.5px;
  }
</style>
</head>
<body>
<main class="stage">
  <section class="card card-front" aria-label="Card front">
    <div class="brand-name">MEDORA CRESTLINE</div>

    <div class="holder">
      <div class="holder-name">Your Name</div>
      <div class="holder-title">Title</div>
    </div>

    <ul class="contact-list">
      <li>
        <svg viewBox="0 0 24 24" aria-hidden="true"><path d="M6.6 10.8a15.1 15.1 0 0 0 6.6 6.6l2.2-2.2c.3-.3.7-.4 1-.2 1.1.4 2.3.6 3.6.6.6 0 1 .4 1 1V20c0 .6-.4 1-1 1A17 17 0 0 1 3 4c0-.6.4-1 1-1h3.5c.6 0 1 .4 1 1 0 1.3.2 2.5.6 3.6.1.3 0 .7-.2 1z"/></svg>
        123-456-0789
      </li>
      <li>
        <svg viewBox="0 0 24 24" aria-hidden="true"><path d="M6 2h9v6H6zM4 9h16a2 2 0 0 1 2 2v9a2 2 0 0 1-2 2H4a2 2 0 0 1-2-2v-9a2 2 0 0 1 2-2zm3 4v2h4v-2zm0 4v2h4v-2zm8-4a1.5 1.5 0 1 0 0 3 1.5 1.5 0 0 0 0-3z"/></svg>
        123-456-0789
      </li>
      <li>
        <svg viewBox="0 0 24 24" aria-hidden="true"><path d="M2 5h20v14H2zm2 2v.5l8 5 8-5V7zm0 2.8V17h16V9.8l-8 5z"/></svg>
        info@medoracrestline.com
      </li>
      <li>
        <svg viewBox="0 0 24 24" aria-hidden="true"><path d="M12 2a10 10 0 1 0 0 20 10 10 0 0 0 0-20zm6.9 6h-3a15 15 0 0 0-1.3-3.9A8 8 0 0 1 18.9 8zM12 4c.8 1.2 1.5 2.5 1.9 4h-3.8c.4-1.5 1.1-2.8 1.9-4zM4.3 14a8 8 0 0 1 0-4h3.4a16 16 0 0 0 0 4zm.8 2h3a15 15 0 0 0 1.3 3.9A8 8 0 0 1 5.1 16zm3-8h-3a8 8 0 0 1 4.3-3.9C8.8 5.3 8.4 6.6 8.1 8zM12 20c-.8-1.2-1.5-2.5-1.9-4h3.8c-.4 1.5-1.1 2.8-1.9 4zm2.3-6H9.7a14 14 0 0 1 0-4h4.6a14 14 0 0 1 0 4zm.3 5.9c.6-1.2 1-2.5 1.3-3.9h3a8 8 0 0 1-4.3 3.9zm1.7-5.9a16 16 0 0 0 0-4h3.4a8 8 0 0 1 0 4z"/></svg>
        www.medoracrestline.com
      </li>
    </ul>

    <address class="address">
      Street Name, City Name<br>
      State Zip Code
    </address>
  </section>

  <section class="card card-back" aria-label="Card back">
    <div class="back-mark">
      <span class="square" aria-hidden="true"></span>
      <span class="brand-name-light">MEDORA CRESTLINE</span>
    </div>
    <div class="back-url">www.medoracrestline.com</div>
  </section>
</main>
</body>
</html>
```